We need a tri-fold brochure for our business called: KindlePath. (KindlePath Therapy Services)
This is a therapy services business that offers Physiotherapy and Occupational Therapy to children aged 5 to 16 years of age. The focus is on Neuro-developmental therapy and the children have a range of conditions such as Cerebral-Palsy, brain injuries etc... We are looking for designs that focus on children, fun and the word nurture.
Target Market(s)
Primarily parents and people looking for therapy services.
Industry/Entity Type
Business
Font styles to use
Sans Serif

```html
<!DOCTYPE html>
<html lang="en">
<head>
<meta charset="utf-8">
<title>KindlePath Therapy Services – Tri-fold Brochure</title>
<link href="https://fonts.googleapis.com/css2?family=Roboto:ital,wght@0,300;0,400;0,700;1,700&display=swap" rel="stylesheet">
<style>
  :root{
    --teal:#0f5b58;
    --teal-dark:#0b3433;
    --teal-text:#1b6a66;
    --orange:#e8661f;
    --ink:#333b3b;
    --paper:#ffffff;
    --backdrop:#1a5b8c;
  }
  *{margin:0;padding:0;box-sizing:border-box}
  html,body{width:1200px;height:1200px;overflow:hidden}
  body{background:var(--backdrop);font-family:'Roboto',sans-serif;position:relative}
  .sheet{position:absolute;background:var(--paper);overflow:hidden;box-shadow:0 14px 18px rgba(0,0,0,.35)}
  .sheet--inside{left:69px;top:53px;width:706px;height:547px}
  .sheet--outside{left:426px;top:622px;width:697px;height:544px}
  .abs{position:absolute}
  .photo{position:absolute}
  .shape-layer{position:absolute;left:0;top:0}

  /* inside sheet */
  .about-label{left:0;width:239px;top:26px;text-align:center;color:var(--orange);font-weight:300;font-size:26px}
  .about-name{left:0;width:239px;top:50px;text-align:center;color:#fff;font-weight:300;font-size:37px}
  .mission-title{left:26px;top:292px;color:var(--teal-text);font-weight:300;font-size:28px}
  .mission-focus{left:26px;top:326px;width:205px;color:var(--ink);font-size:14.5px;line-height:18px;text-transform:uppercase}
  .mission-focus small{font-size:10px}
  .mission-body{left:26px;top:463px;width:192px;color:var(--teal-text);font-size:10.5px;line-height:13px;text-align:justify}
  .approach-title{left:257px;top:48px;color:var(--teal);font-size:21px}
  .approach-list{left:257px;top:80px;width:196px;list-style:none;color:var(--ink);font-size:10.3px;line-height:12.8px}
  .approach-list li{margin-bottom:12.5px}
  .approach-list li::before{content:"• "}
  .space-title{left:278px;top:343px;width:175px;text-align:center;color:#fff;font-size:20px}
  .space-body{left:279px;top:379px;width:172px;color:#fff;font-size:10.2px;line-height:12.7px;text-align:justify}
  .location-title{left:487px;top:385px;width:198px;text-align:center;color:#fff;font-size:20px}
  .location-body{left:487px;top:419px;width:198px;color:#fff;font-size:10.2px;line-height:12.7px;text-align:justify}
  .location-body p{margin-bottom:12px}

  /* outside sheet */
  .cover-name{left:0;width:233px;top:14px;text-align:center;color:var(--teal);font-weight:300;font-size:30px}
  .cover-tagline{left:0;width:233px;top:46px;text-align:center;color:var(--orange);font-size:10.5px}
  .cover-intro{left:20px;width:193px;top:66px;text-align:center;color:var(--teal-text);font-size:10.4px;line-height:12.7px}
  .cover-intro p{margin-bottom:12px}
  .offer-title{left:0;width:233px;top:295px;text-align:center;color:#fff;font-size:23px}
  .offer-list{left:0;width:233px;top:351px;text-align:center;color:#fff;font-size:10.4px;line-height:12.7px;list-style:none}
  .offer-list .gap{margin-top:12px}
  .offer-note{left:22px;width:189px;top:482px;text-align:center;color:#fff;font-size:7.4px;line-height:9.5px}
  .contact-brand{left:233px;width:232px;top:350px;text-align:center}
  .contact-block{left:233px;width:232px;top:339px;text-align:center;color:#fff;font-size:10.4px;line-height:12.7px}
  .contact-block p{margin-bottom:12px}
  .contact-block em{font-weight:700}
  .contact-lines{color:#8fd3cf;line-height:21px}
  .contact-note{left:247px;width:204px;top:486px;text-align:center;color:#fff;font-size:6.6px;line-height:8.2px}
  .brand-dot{left:548px;top:28px;width:48px;height:48px;border-radius:50%;background:var(--teal)}
  .brand-name{left:465px;width:232px;top:75px;text-align:center;color:var(--teal);font-weight:300;font-size:28px}
  .brand-sub{left:465px;width:232px;top:106px;text-align:center;color:#5d6c6c;font-weight:300;font-size:12px;letter-spacing:2px}
  .services-hero{left:465px;width:232px;top:404px;text-align:center;color:#fff}
  .services-hero .big{font-size:21.5px;line-height:24px;letter-spacing:.3px}
  .services-hero .and{font-size:12px;line-height:14px;margin-bottom:5px}
  .services-hero .small{font-size:12.5px;line-height:15px}
</style>
</head>
<body>

<!-- Inside spread -->
<section class="sheet sheet--inside" aria-label="Brochure inside spread">
  <div class="photo" role="img" aria-label="Photo of a boy and a therapist working together at a laptop in a library" style="left:0;top:100px;width:239px;height:230px;background:linear-gradient(180deg,#8a6a4c 0%,#c98d7a 45%,#e6d6cf 75%,#f4f4f2 100%)"></div>
  <div class="photo" role="img" aria-label="Photo of two children building with colourful blocks in a classroom" style="left:471px;top:0;width:235px;height:380px;background:linear-gradient(160deg,#d7dde0 0%,#b8c2c6 40%,#e7e1da 70%,#8c9aa0 100%)"></div>
  <div class="abs" style="left:239px;top:0;width:232px;height:547px;background:linear-gradient(90deg,#e8eaea 0%,#fff 25%)"></div>

  <svg class="shape-layer" width="706" height="547" viewBox="0 0 706 547" aria-hidden="true">
    <path d="M0,0 H271 C258,70 220,113 150,113 H0 Z" fill="var(--teal)"/>
    <path d="M239,0 H271 C262,40 250,70 239,80 Z" fill="var(--teal-dark)"/>
    <path d="M0,330 H239 V547 H0 Z" fill="#fbfbfb"/>
    <path d="M258,547 C220,430 300,302 440,302 C510,302 548,340 570,366 C610,343 668,343 706,368 V547 Z" fill="var(--teal)"/>
    <circle cx="279" cy="307" r="29" fill="var(--orange)"/>
  </svg>

  <div class="abs about-label">About</div>
  <h1 class="abs about-name">KindlePath</h1>

  <h2 class="abs mission-title">Our Mission</h2>
  <p class="abs mission-focus">The focus is on neuro-developmental therapy and the children have a range of conditions such as cerebral-palsy, brain injuries <small>etc.....</small></p>
  <p class="abs mission-body">KindlePath Kids is to help children gain strength, confidence and freedom of movement. We do this by constantly working to:</p>

  <h2 class="abs approach-title">Our Approach</h2>
  <ul class="abs approach-list">
    <li>We provide compassionate, family-centered therapy that is fun and engaging for children.</li>
    <li>We support parents and families with ongoing education and resources.</li>
    <li>We offer personalized service and wide range of therapies to meet the specific needs of each child and family.</li>
    <li>We integrate therapy into various aspects of each child and family's life, to maximize the benefit for each child.</li>
  </ul>

  <h2 class="abs space-title">Our Space</h2>
  <p class="abs space-body">We offer children and families a unique and highly engaging clinic setting that includes a 1500 square foot gym filled with a wide range of climbing, gross motor and sensory equipment. This includes monkey bars, zip line, climbing wall, climbing net, suspension equipment, and a host of other equipment for kids of all abilities to build skills and have fun.</p>

  <h2 class="abs location-title">Our Location</h2>
  <div class="abs location-body">
    <p>We are located at 48 Maplebrook Lane, Cedar Falls.</p>
    <p>We have direct street level access with ample free street parking right out front and additional parking at the rear of our clinic.</p>
  </div>
</section>

<!-- Outside spread -->
<section class="sheet sheet--outside" aria-label="Brochure outside spread">
  <div class="photo" role="img" aria-label="Photo of a row of smiling children in bright colourful shirts" style="left:0;top:176px;width:233px;height:120px;background:linear-gradient(90deg,#f2d25a 0%,#f08a3a 25%,#e04a8a 50%,#4aa3d8 75%,#eef3f5 100%)"></div>
  <div class="photo" role="img" aria-label="Photo of a smiling boy against a green garden background" style="left:233px;top:0;width:232px;height:544px;background:linear-gradient(180deg,#6e8a3a 0%,#9a7a4e 25%,#d9a58a 42%,#1f5c45 62%,var(--teal-dark) 80%)"></div>
  <div class="photo" role="img" aria-label="Photo of a young child in glasses pointing upward" style="left:465px;top:0;width:232px;height:380px;background:linear-gradient(180deg,#f1f3f3 0%,#e6eaeb 40%,#e8c8a8 60%,#a9c3d8 100%)"></div>

  <svg class="shape-layer" width="697" height="544" viewBox="0 0 697 544" aria-hidden="true">
    <path d="M0,281 C80,278 170,282 233,292 V544 H0 Z" fill="var(--teal-dark)"/>
    <path d="M0,332 C80,325 170,322 233,338 V544 H0 Z" fill="var(--teal)"/>
    <path d="M465,382 C540,374 620,368 697,374 V544 H465 Z" fill="var(--teal-dark)"/>
    <path d="M465,387 C540,380 620,376 697,382 V544 H465 Z" fill="var(--teal)"/>
  </svg>

  <h1 class="abs cover-name">KindlePath</h1>
  <p class="abs cover-tagline">Fun, Engaging Therapy for Kids</p>
  <div class="abs cover-intro">
    <p>KindlePath Kids offers comprehensive therapy services for infants, children and teens within an environment to inspire success!</p>
    <p>We are here to help families and children with a wide range of abilities to reach their goals.</p>
  </div>

  <h2 class="abs offer-title">We offer.</h2>
  <ul class="abs offer-list">
    <li>Physiotherapy</li>
    <li>Sport Therapy</li>
    <li>Occupational Therapy</li>
    <li class="gap">Speech Language Therapy</li>
    <li>Dietitian and Nutrition Services</li>
    <li class="gap">Child and Family</li>
    <li>Psychology Services</li>
  </ul>
  <p class="abs offer-note">Comprehensive physiotherapy and occupational therapy services for infants, children and teens with a wide range of abilities and diagnoses.</p>

  <div class="abs" style="left:325px;top:278px;width:48px;height:48px;border-radius:50%;background:#fff"></div>
  <div class="abs contact-block">
    <p>We are always happy to answer your questions!</p>
    <p>For more information or to<br><em>BOOK AN APPOINTMENT,</em><br>CONTACT US AT:</p>
    <div class="contact-lines">
      Tel: 555-014-2870<br>
      Fax: 555-014-2871<br>
      eMail: hello@kindlepath.example
    </div>
  </div>
  <p class="abs contact-note">PLEASE NOTE:<br>We will respond to all email and telephone inquiries as promptly as possible. We will always be sure to respond by the next business day.</p>

  <div class="abs brand-dot"></div>
  <div class="abs brand-name">KindlePath</div>
  <div class="abs brand-sub">Therapy Services</div>

  <div class="abs services-hero">
    <div class="big">PHYSIOTHERAPY</div>
    <div class="and">and</div>
    <div class="big">OCCUPATIONAL</div>
    <div class="small">Therapy to children aged<br>5 to 16 years of age</div>
  </div>
</section>

</body>
</html>
```